Wine Bottle Label Logo Design

My fiancé and I are getting married in September and we made homemade wine which will be given to the guests as a wedding favor. We need label/logo for our wine bottles. We were looking for something rustic yet modern and simple. We had an idea for beige and cranberry colored wine stained, weathered, imperfect heart. Things that will need to be incorporated into the label design are as follows:
Our last name and also the name of the wine: Fusaldi
The year: 2012
Where is says Alcohol Content on a wine bottle normally write: Alcohol: Deceiving% by vol.
Type of wine: Red Wine
Incorporate our wedding date: Foot Stomped and Bottled for Nadia and Gus's Wedding Day 9/28/13
Wedding

```html
<!DOCTYPE html>
<html lang="en">
<head>
<meta charset="utf-8">
<title>Fusaldi Wedding Wine Label</title>
<link rel="stylesheet" href="https://fonts.googleapis.com/css2?family=Poppins:wght@800&family=Josefin+Sans:wght@600;700&family=Limelight&family=Federo&family=Lato:ital,wght@1,400;1,700&display=swap">
<style>
  :root {
    --page: #ffffff;
    --label-cream: #f8f0dc;
    --label-border: #c9545e;
    --ink: #111111;
    --cranberry: #b01e3a;
    --wine-dark: #7b1d2a;
  }
  * { margin: 0; padding: 0; box-sizing: border-box; }
  html, body {
    width: 927px;
    height: 1200px;
    overflow: hidden;
    background: var(--page);
  }
  .canvas {
    position: relative;
    width: 927px;
    height: 1200px;
  }
  .wine-label {
    position: absolute;
    left: 72px;
    top: 181px;
    width: 783px;
    height: 838px;
    background: var(--label-cream);
    border: 3px solid var(--label-border);
  }
  .wine-label > * { position: absolute; white-space: nowrap; }
  .family-name {
    left: 0; right: 0;
    top: 4px;
    text-align: center;
    font-family: "Poppins", sans-serif;
    font-weight: 800;
    font-size: 168px;
    line-height: 1;
    letter-spacing: 2px;
    color: var(--ink);
  }
  .vintage {
    left: 0; right: 0;
    top: 170px;
    text-align: center;
    font-family: "Federo", sans-serif;
    font-size: 38px;
    letter-spacing: 6px;
    color: var(--ink);
  }
  .process {
    left: 0; right: 0;
    top: 214px;
    text-align: center;
    font-family: "Josefin Sans", sans-serif;
    font-weight: 700;
    font-size: 82px;
    line-height: 1;
    letter-spacing: 1px;
    color: var(--wine-dark);
  }
  .dedication {
    left: 98px;
    top: 300px;
    transform-origin: left top;
    transform: translateX(48px) rotate(90deg);
    font-family: "Josefin Sans", sans-serif;
    font-weight: 700;
    font-size: 50px;
    line-height: 1;
    letter-spacing: 2px;
    color: var(--wine-dark);
  }
  .dedication .for { font-size: 36px; color: var(--ink); }
  .couple-name {
    left: 258px;
    font-family: "Limelight", sans-serif;
    font-size: 104px;
    line-height: 1;
    color: var(--cranberry);
  }
  .couple-first { top: 318px; }
  .couple-second { top: 462px; }
  .ampersand {
    left: 298px;
    top: 420px;
    font-family: "Limelight", sans-serif;
    font-size: 44px;
    line-height: 1;
    color: var(--cranberry);
  }
  .occasion {
    left: 254px;
    top: 588px;
    font-family: "Josefin Sans", sans-serif;
    font-weight: 700;
    font-size: 56px;
    line-height: 1;
    color: var(--ink);
  }
  .wedding-date {
    left: 258px;
    top: 652px;
    font-family: "Josefin Sans", sans-serif;
    font-weight: 700;
    font-size: 44px;
    line-height: 1;
    color: var(--cranberry);
  }
  .tasting-note {
    left: 0; right: 0;
    top: 732px;
    text-align: center;
    font-family: "Lato", sans-serif;
    font-style: italic;
    font-weight: 700;
    font-size: 17.5px;
    line-height: 1.45;
    color: var(--ink);
    white-space: normal;
  }
  .alcohol {
    left: 0; right: 0;
    top: 796px;
    text-align: center;
    font-family: "Lato", sans-serif;
    font-style: italic;
    font-size: 19px;
    color: var(--cranberry);
  }
</style>
</head>
<body>
  <main class="canvas">
    <section class="wine-label">
      <h1 class="family-name">FUSALDI</h1>
      <p class="vintage">2012</p>
      <p class="process">FOOT—STOMPED</p>
      <p class="dedication">&amp; BOTTLED <span class="for">FOR</span></p>
      <p class="couple-name couple-first">Nadia</p>
      <p class="ampersand">&amp;</p>
      <p class="couple-name couple-second">Gus’s</p>
      <p class="occasion">WEDDING DAY</p>
      <p class="wedding-date">9/28/13</p>
      <p class="tasting-note">Aged outdoors during the cold winter months to allow for a<br>slower fermentation process. It’s like a warm, sweet hug in a bottle.</p>
      <p class="alcohol">Alcohol: Deceiving % by vol.</p>
    </section>
  </main>
</body>
</html>
```